Billboard design for a small town Oral Surgeon

We are getting several billboards and need a design that highlights the doctors photo, and bullet points of what he does. Our business name is extremely long, so it’s a challenge to figure out how to do this. Maybe just use our logo? Open to ideas.
The logo can be shortened as designer sees fit, meaning we can drop the tag line. Important info to include:
Doctors name is Tobin Marek
The highlighted bullet points are:
•Implants
•wisdom teeth
•Jaw Surgery
•facial trauma
The goal of this billboard is to let our community know that they have an option here in Ada, our town. Many still drive to the city a couple hours away not knowing they now have an option here at home. Having a hard time finding examples of what I have in mind, so hoping this will get us going. I want it as “non-busy” as possible, so no unnecessary lines or anything that competes with the information we are trying to get across.

Target Market(s)

Everyone in town, just trying to spread the word that we are here

Industry/Entity Type

Medical/surgical (oral surgery)

Font styles to use
Sans Serif

Colors
0094D4
00A9DD
6FCCEA
C7EBF8
E9F6FB

Requirements
Must have
• *New note** Due to location of billboard, I prefer the photo of doctor to be on the left side. Must look neat and professional. Must highlight what we do.
Nice to have
• Our colors are a blue-green with silver, against black or white, but I’m flexible on this, I don’t necessarily need the colors highlighted. I’m also flexible on font style, just needs to be easy to read.
Should not have
• Distracting graphics, should not look like a dental office. That’s an issue we have is people thinking we are another dental office, we do not do any general dentistry, it’s surgery only.

```html
<!DOCTYPE html>
<html lang="en">
<head>
<meta charset="utf-8">
<title>Tobin Marek – Oral Surgery Billboard</title>
<link rel="stylesheet" href="https://fonts.googleapis.com/css2?family=Nunito+Sans:ital,wght@0,400;0,600;0,700;1,700&display=swap">
<style>
  :root {
    --page-bg: #ececec;
    --board-white: #ffffff;
    --board-sheen: #f1f2f3;
    --teal: #168fa8;
    --teal-light: #1e9db6;
    --ink: #3a3f44;
    --photo-dark: #1f2a3a;
    --photo-mid: #6b7480;
    --photo-light: #d9c3b4;
    --text-light: #ffffff;
  }
  * { box-sizing: border-box; margin: 0; padding: 0; }
  html, body {
    width: 1200px; height: 1200px; overflow: hidden;
    background: var(--page-bg);
    font-family: "Nunito Sans", Arial, sans-serif;
  }
  .billboard {
    position: absolute; left: 90px; top: 345px;
    width: 1022px; height: 511px;
    background:
      linear-gradient(155deg, transparent 0 38%, var(--board-sheen) 38% 52%, transparent 52%),
      linear-gradient(155deg, var(--board-white) 0 60%, var(--board-sheen) 60% 70%, var(--board-white) 70%);
    overflow: hidden;
    box-shadow: 0 2px 6px rgba(0,0,0,0.12);
  }
  .service-band {
    position: absolute; left: 0; top: 259px;
    width: 100%; height: 211px;
    background: linear-gradient(90deg, var(--teal) 0%, var(--teal-light) 100%);
  }
  .doctor-photo {
    position: absolute; left: 0; top: 49px;
    width: 344px; height: 462px;
    border-top-right-radius: 40px;
    background: linear-gradient(180deg, var(--photo-light) 0%, var(--photo-mid) 45%, var(--photo-dark) 75%);
  }
  .doctor-name {
    position: absolute; left: 366px; top: 274px;
    color: var(--text-light);
    font-weight: 700; font-style: italic;
    font-size: 29px; line-height: 36px; letter-spacing: 0.3px;
    white-space: nowrap;
  }
  .services {
    position: absolute; right: 87px; top: 282px;
    list-style: none; text-align: right;
    color: var(--text-light);
    font-weight: 700; font-size: 31px; line-height: 40.5px;
    white-space: nowrap;
  }
  .practice-mark {
    position: absolute; left: 720px; top: 48px;
    width: 240px; text-align: center;
  }
  .practice-dot {
    width: 80px; height: 80px; border-radius: 50%;
    background: var(--teal);
    margin: 0 auto 14px;
  }
  .practice-name {
    color: var(--ink);
    font-weight: 400; font-size: 15px; line-height: 19px;
    text-transform: uppercase;
  }
</style>
</head>
<body>
  <main class="billboard">
    <div class="service-band"></div>
    <div class="doctor-photo" role="img" aria-label="Portrait photo of the surgeon in a dark suit and red tie, smiling"></div>
    <h1 class="doctor-name">Tobin Marek</h1>
    <ul class="services">
      <li>Implants</li>
      <li>Wisdom teeth</li>
      <li>Jaw Surgery</li>
      <li>Facial trauma</li>
    </ul>
    <div class="practice-mark">
      <div class="practice-dot"></div>
      <p class="practice-name">Red River Oral<br>&amp; Facial Surgery</p>
    </div>
  </main>
</body>
</html>
```